Book Cover in a 6x9 inches size for BEFORE THE LANTERNS FADE

Instructions for creating a 6x9 inches book cover to be uploaded on PressVellum:
1. I am not sure what I want for a book cover. Hope you can put your
creative mind to work to think of something unique and creative as a
book cover with the photos I've provided ☺
2. Let me explain a bit so that you understand what the book is about:
The Title: BEFORE THE LANTERNS FADE.
The title comes from the Bible verse Luke 19:37-40 about Jesus’ last
ride into Jerusalem before His crucifixion, when a multitude of
disciples were rejoicing and praising God for all the mighty works that
they had seen. The Pharisees (who were the religious authorities of the
Jews) said to Jesus: “Master, rebuke thy disciples”. He said unto them: “I
tell you that, if these should hold their peace, the stones would
immediately cry out.”
It really means when people who were created by Almighty God do not
want to praise and worship Him, creation will, as mentioned in different
sections in the Bible. In this particular verse Jesus said if the people are
not going to praise Him, the stones will. It came from a time that I was
sad to see how few people at my workplace wanted to know about God,
let alone serve Him. The Bible verses painted on the river stones are
about my stone ministry that I’ve started on earth. This is a symbol of
when God’s people do not want to praise Him, I’ll make sure the stones
will cry out, resembling what Jesus said in Luke 19:37-40. I use Bible
verses to praise God, to break the curses on the land, for protection, and
for blessings.
2. I have uploaded 3 preferred photos (that were edited and the colors
enhanced) which I think will work best. But I also uploaded three other
photos which were not edited if you think that you can use them to help
your creation idea. The one photo of the stones that have enough white
space between them was taken with the idea if you want to have it
separated to make your own design.
3. The main aim is for people to see how the painted stones look like that I
use in my stone ministry. When they read the ‘Forward’ of the book it
will be clear what the meaning of the painted stones on the book cover
is.
4. I am looking forward to receive a beautiful book cover. Do not hesitate
to send me a message if you have any questions or need clarification.
Thank you 😊
Christians

```html
<!DOCTYPE html>
<html lang="en">
<head>
<meta charset="utf-8">
<title>Before the Lanterns Fade — Cover</title>
<link rel="stylesheet" href="https://fonts.googleapis.com/css2?family=Cinzel:wght@400;500&family=Crimson+Text:ital@1&display=swap">
<style>
  :root {
    --page-bg: #ffffff;
    --night-navy: #1c2f6b;
    --deep-navy: #14224f;
    --storm-violet: #5a4a8c;
    --storm-lilac: #a28cc4;
    --horizon-glow: #e7a884;
    --stone-dark: #2a2733;
    --copper-light: #f1c9a8;
    --copper-mid: #c88a62;
    --copper-deep: #9c5f3c;
    --band-ink: #2b1a12;
    --text-light: #ffffff;
  }
  * { margin: 0; padding: 0; box-sizing: border-box; }
  html, body {
    width: 1200px;
    height: 960px;
    overflow: hidden;
    background: var(--page-bg);
  }
  .canvas {
    width: 1200px;
    height: 960px;
    display: flex;
    align-items: center;
    justify-content: center;
  }
  .cover {
    position: relative;
    width: 600px;
    height: 900px;
    overflow: hidden;
    background: var(--deep-navy);
  }
  .cover-scene {
    position: absolute;
    inset: 0 0 118px 0;
    background:
      radial-gradient(ellipse 40% 18% at 60% 74%, rgba(240,190,160,0.85), rgba(240,190,160,0) 70%),
      linear-gradient(180deg,
        var(--deep-navy) 0%,
        var(--night-navy) 38%,
        var(--storm-violet) 55%,
        var(--storm-lilac) 68%,
        var(--horizon-glow) 77%,
        #6d5a78 83%,
        var(--stone-dark) 100%);
  }
  .cover-text {
    position: absolute;
    inset: 0;
    text-align: center;
    color: var(--text-light);
  }
  .tagline {
    margin: 62px auto 0;
    width: 500px;
    font-family: "Crimson Text", Georgia, serif;
    font-style: italic;
    font-size: 21px;
    line-height: 1.35;
    transform: rotate(-2.5deg);
  }
  .title {
    margin-top: 36px;
    font-family: "Cinzel", "Times New Roman", serif;
    font-weight: 400;
    line-height: 1;
  }
  .title-line { display: block; }
  .title-top {
    font-size: 58px;
    letter-spacing: 2px;
  }
  .title-key {
    margin-top: 6px;
    font-size: 92px;
    background: linear-gradient(180deg, var(--copper-light) 0%, var(--copper-mid) 55%, var(--copper-deep) 100%);
    -webkit-background-clip: text;
    background-clip: text;
    color: transparent;
  }
  .title-bottom {
    margin-top: 8px;
    font-size: 66px;
    letter-spacing: 2px;
  }
  .author-band {
    position: absolute;
    left: 0;
    right: 0;
    bottom: 0;
    height: 118px;
    display: flex;
    align-items: center;
    justify-content: center;
    background: linear-gradient(90deg, var(--copper-deep) 0%, var(--copper-light) 45%, var(--copper-mid) 75%, var(--copper-deep) 100%);
  }
  .author-name {
    font-family: "Cinzel", "Times New Roman", serif;
    font-weight: 500;
    font-size: 36px;
    letter-spacing: 6px;
    color: var(--band-ink);
  }
</style>
</head>
<body>
  <main class="canvas">
    <article class="cover">
      <div class="cover-scene" role="img" aria-label="Stormy violet sky with lightning over a glowing sea horizon and dark river stones along the shore"></div>
      <div class="cover-text">
        <p class="tagline">A call to wholehearted praise, and ancient<br>promises to help you keep watch for the<br>coming dawn and the return of the King.</p>
        <h1 class="title">
          <span class="title-line title-top">BEFORE THE</span>
          <span class="title-line title-key">LANTERNS</span>
          <span class="title-line title-bottom">FADE</span>
        </h1>
      </div>
      <footer class="author-band">
        <p class="author-name">MARLA VENTER</p>
      </footer>
    </article>
  </main>
</body>
</html>
```